PLUM BUSINESS CARD

Need a business card and logo. The company name is PLUM (Piedmont League of Ultimate Mareriders). It's a business that offers horseback riding lessons to young girls. Please put my name: Renata Bowley and a place for email and phone number. I would like the card to look feminine and soft. I like script type lettering. I want the card to be white or ivory with black or gray and hot pink print. A horse head outline would be cool, something whimsical. Think teen girl who likes glamour. Also, I give western riding lessons. So I like faded out background Images of western saddles, cowgirls, horses with long hair, ropes, horses in sunset...mabe the word PLUM can be made out of a lasso rope?

Just updated my project with a little more detail

Target Market(s)

Young girls/ cowgirls, western riding

Industry/Entity Type

Horseback Riding

Font styles to use
Script

Colors
e34197

Requirements
Must have
• A logo of PLUM.
Must say Piedmont League of Ultimate Mareriders
Colors are Pink and Black with an elegant, glamorous, feminine look.
Nice to have
• Could have a picture or outline of a horse

```html
<!DOCTYPE html>
<html lang="en">
<head>
<meta charset="utf-8">
<title>PLUM Business Card</title>
<link rel="stylesheet" href="https://fonts.googleapis.com/css2?family=Cormorant+Garamond:ital,wght@0,500;1,400;1,500&display=swap">
<style>
  :root {
    --pink-top: #ee8ae0;
    --pink-mid: #f4b6ea;
    --card-white: #fbf7fa;
    --hot-pink: #f21fb8;
    --ink: #140a12;
    --name-ink: #3a1a30;
    --silhouette: #121012;
  }
  * { margin: 0; padding: 0; box-sizing: border-box; }
  html, body {
    width: 1200px;
    height: 686px;
    overflow: hidden;
    background: var(--card-white);
  }
  .card {
    position: relative;
    width: 1200px;
    height: 686px;
    overflow: hidden;
    background: linear-gradient(180deg, var(--pink-top) 0%, var(--pink-mid) 50%, var(--card-white) 100%);
    font-family: "Cormorant Garamond", Georgia, serif;
  }
  .brand-name {
    position: absolute;
    left: 0;
    top: 6px;
    width: 1280px;
    text-align: center;
    font-size: 196px;
    font-weight: 500;
    line-height: 1;
    letter-spacing: 34px;
    color: var(--hot-pink);
  }
  .brand-arc {
    position: absolute;
    left: 0;
    top: 0;
    width: 1200px;
    height: 340px;
  }
  .brand-arc text {
    font-family: "Cormorant Garamond", Georgia, serif;
    font-style: italic;
    font-weight: 500;
    font-size: 37px;
    fill: var(--ink);
  }
  .rider-figure {
    position: absolute;
    left: 436px;
    top: 232px;
    width: 364px;
    height: 454px;
    border-radius: 140px 160px 30px 30px;
    background: radial-gradient(ellipse at 55% 45%, var(--silhouette) 60%, rgba(18,16,18,0.85) 100%);
  }
  .contact {
    position: absolute;
    left: 22px;
    top: 474px;
    color: var(--ink);
  }
  .contact-name {
    font-size: 56px;
    font-style: italic;
    font-weight: 400;
    color: var(--name-ink);
    line-height: 1;
    margin-bottom: 30px;
  }
  .contact-line {
    font-size: 38px;
    font-style: italic;
    font-weight: 400;
    line-height: 55px;
  }
</style>
</head>
<body>
  <main class="card">
    <div class="brand-name">PLUM</div>
    <svg class="brand-arc" viewBox="0 0 1200 340" aria-hidden="false">
      <path id="tagline-curve" d="M250,300 Q640,66 1020,306" fill="none"/>
      <text>
        <textPath href="#tagline-curve" startOffset="50%" text-anchor="middle" textLength="820" lengthAdjust="spacingAndGlyphs">Piedmont League of Ultimate Mareriders</textPath>
      </text>
    </svg>
    <div class="rider-figure" role="img" aria-label="Black silhouette of a cowgirl in a hat walking beside her horse, holding the lead rope"></div>
    <section class="contact">
      <h1 class="contact-name">Renata Bowley</h1>
      <p class="contact-line">Phone: (xxx) xxx-xxxx</p>
      <p class="contact-line">Email: sample@email.com</p>
    </section>
  </main>
</body>
</html>
```